Flyer für Vermietung und Verkauf von Hüpfburgen, aufblasbaren Festzelten und aufblasbaren Hindernisparcours
Zielgruppe
Wir vermieten und verkaufen Hüpfburgen, aufblasbare Festzelte und aufblasbare Hindernisparcours. Ebenso Sport- und Fungeräte mit Augmented Reality. Für den aktuelen Flyer sollen Vereine, Städte, Gemeinden und Private für den Fasching angesprochen werden.
Aufgabenstellung
Der Flyer soll A4 sein mit 6 Bildern.
Als Text soll enthalten sein:
Slogan: Ihre Faschingsparty mit unseren aufblasbaren Highlights (bessere Ideen sind gerne gefragt)
Text: Machen Sie mit unseren aufblasbaren Hinguckern Ihre Faschingsparty zum absoluten Highlight.
Ganz gleich, ob in der Firma oder privat, für jeden Anlass bieten wir die passende Ergänzung.
Spiele, Hüpfburgen, Sport-Parcours oder Festzelte mit Beleuchtung, wir bieten Ihnen unbegrenzte Möglichkeiten für Ihre Party.
Kontakt:
Bei Interesse kontaktieren Sie uns bitte via Email!
Renate Wolkner re.wolkner@pumpflor.biz
Brenzach (Germany) - Lorbrunn (Austria)

```html
<!DOCTYPE html>
<html lang="de">
<head>
<meta charset="utf-8">
<title>pumpflor – Faschingsparty Flyer</title>
<link rel="stylesheet" href="https://fonts.googleapis.com/css2?family=Bebas+Neue&family=Montserrat:wght@700&family=Figtree:wght@400;500&display=swap">
<style>
  :root {
    --paper: #ffffff;
    --ink: #1f1f1f;
    --muted: #4a4a4a;
    --headline: #f26a1b;
    --headline-edge: #ffffff;
    --headline-shadow: rgba(60, 20, 0, 0.55);
  }
  * { box-sizing: border-box; margin: 0; padding: 0; }
  html, body { width: 849px; height: 1200px; overflow: hidden; background: var(--paper); }
  .flyer {
    position: relative;
    width: 849px;
    height: 1200px;
    background: var(--paper);
    color: var(--ink);
    font-family: "Figtree", "Helvetica Neue", Arial, sans-serif;
    overflow: hidden;
  }
  .paint-backdrop {
    position: absolute;
    left: 0; top: 0;
    width: 849px; height: 440px;
    background:
      linear-gradient(200deg, rgba(255,255,255,0) 45%, rgba(255,255,255,0.95) 82%),
      linear-gradient(115deg, #e8421f 0%, #f7a21a 14%, #f4e21c 26%, #8ccf2a 38%, #2fb24a 48%, #1fb7c9 60%, #1c6fd6 72%, #4a3fcf 84%, #a23ee0 100%);
  }
  .headline {
    position: absolute;
    left: 0; top: 140px;
    width: 100%;
    font-family: "Bebas Neue", Impact, sans-serif;
    font-weight: 400;
    color: var(--headline);
    -webkit-text-stroke: 1.5px var(--headline-edge);
    text-shadow: 2px 3px 6px var(--headline-shadow);
  }
  .headline__kicker {
    position: absolute; left: 41px; top: 2px;
    font-size: 42px; line-height: 1; white-space: nowrap; letter-spacing: 0.3px;
  }
  .headline__main {
    position: absolute; left: 41px; top: 50px;
    font-size: 88px; line-height: 90px; white-space: nowrap;
  }
  .intro {
    position: absolute; left: 0; top: 406px; width: 849px;
    text-align: center; font-size: 27px; line-height: 34px; font-weight: 500;
  }
  .offer-list {
    position: absolute; left: 140px; top: 505px; list-style: none;
    font-family: "Montserrat", Arial, sans-serif; font-weight: 700; font-size: 26px;
  }
  .offer-list li { display: flex; align-items: center; height: 41.5px; white-space: nowrap; }
  .offer-list .box {
    width: 21px; height: 21px; border: 3px solid var(--ink); margin-right: 14px;
    display: flex; align-items: center; justify-content: center; flex: none;
  }
  .offer-list .box::after { content: ""; width: 8px; height: 8px; background: var(--ink); }
  .closing {
    position: absolute; left: 0; top: 697px; width: 849px;
    text-align: center; font-size: 27px; line-height: 36px; font-weight: 500;
  }
  .contact { position: absolute; left: 26px; top: 865px; }
  .contact__call { font-size: 27px; line-height: 34px; font-weight: 500; }
  .contact__details { margin-top: 8px; font-size: 18px; line-height: 25px; }
  .brand {
    position: absolute; left: 30px; top: 1066px;
    font-family: "Figtree", Arial, sans-serif; font-weight: 500;
    font-size: 46px; line-height: 1; color: var(--ink);
  }
  .brand__tagline {
    position: absolute; left: 150px; top: 1123px;
    font-size: 20px; line-height: 25px; color: var(--muted);
  }
  .brand__tagline span { display: block; padding-left: 60px; }
  .product-collage { position: absolute; left: 381px; top: 798px; width: 468px; height: 402px; }
</style>
</head>
<body>
<main class="flyer">
  <div class="paint-backdrop" role="img" aria-label="Bunte diagonale Farbpinselstriche in Regenbogenfarben"></div>

  <h1 class="headline">
    <span class="headline__kicker">Machen Sie mit unseren aufblasbaren Hinguckern</span>
    <span class="headline__main">Ihre Faschingsparty zum<br>absoluten Highlight.</span>
  </h1>

  <p class="intro">Ganz gleich, ob in der Firma oder privat, für jeden<br>Anlass bieten wir die passende Ergänzung.</p>

  <ul class="offer-list">
    <li><span class="box"></span>SPIELE,</li>
    <li><span class="box"></span>HÜPFBURGEN,</li>
    <li><span class="box"></span>SPORT-PARCOURS ODER</li>
    <li><span class="box"></span>FESTZELTE MIT BELEUCHTUNG,</li>
  </ul>

  <p class="closing">wir bieten Ihnen unbegrenzte Möglichkeiten für Ihre<br>Party.</p>

  <section class="contact">
    <p class="contact__call">Bei Interesse kontaktieren<br>Sie uns bitte via Email!</p>
    <p class="contact__details">Renate Wolkner re.wolkner@pumpflor.biz<br>Brenzach (Germany) - Lorbrunn (Austria)</p>
  </section>

  <p class="brand">pumpflor</p>
  <p class="brand__tagline">Gut gelaunt –<span>gut gefeiert</span></p>

  <svg class="product-collage" role="img" aria-label="Collage aufblasbarer Produkte: Tiki-Bar, Feuerwehr-Hüpfburg, Blockhütte, Krokodil-Hüpfburg, Ente und Rutsche" viewBox="0 0 468 402">
    <defs>
      <radialGradient id="collageTone" cx="0.55" cy="0.6" r="0.7">
        <stop offset="0" stop-color="#f2c43a"/>
        <stop offset="0.45" stop-color="#d9603a"/>
        <stop offset="0.8" stop-color="#5c8a3a"/>
        <stop offset="1" stop-color="#ffffff"/>
      </radialGradient>
    </defs>
    <rect width="468" height="402" fill="url(#collageTone)"/>
  </svg>
</main>
</body>
</html>
```